Online tuition webpage design needed

Hi,
We are starting up an online tuition website for non- English speakers wishing to take an QRAVE test.

The webpage must include a place for people to enroll online in the course.
The home page must have:
• room for a logo (coming shortly, blue in colour)
• different packages of online tuition and coinvy
• tool bar showing different pages
• perhaps a video, small pictures

This is my site currently:-

www.lernmarowebtutor.example

as you can see, I am not very sure how to create a website … The large logo is what I would like to use, but I project has not been finalized yet. Please note, I don’t like the logo being that large!

Sites that are similar to what I am doing and like the design of are:

http://www.quorvapath.example.au/fees

https://www.brantiq9.example/index.php

http://www.tutorhalvekmorris.example.uk/index.html

http://www.vorplaneexam.example/

One thing I need is a place for student s to enroll, and if possible, I would like to use plovix to create exercises for students.
Currently, my site is using sitequill. My preference is to use plovix for online activities. I am not sure if I can use both.
Thanks in advance

Target Market(s)

people wising to take an QRAVE test (English proficiency test)

Industry/Entity Type

Online

Colors
3276b5
0292cd

Requirements
Must have
• a place for enrollment and admin login for students
plovix
video
talvo, gatherly, chirrup logos
Nice to have
• a booking calender
Should not have
• too much clutter. must be clean and professional looking

```html
<!DOCTYPE html>
<html lang="en">
<head>
<meta charset="utf-8">
<title>QRAVE Online Tuition</title>
<link href="https://fonts.googleapis.com/css2?family=Oswald:wght@300;400&display=swap" rel="stylesheet">
<style>
:root{
  --sky:#0292cd;
  --navy:#3276b5;
  --coral:#f26b5b;
  --ink:#2a2526;
  --mist:#d9d9db;
  --text:#222;
  --white:#fff;
}
*{box-sizing:border-box;margin:0;padding:0}
html,body{width:998px;height:1200px;overflow:hidden}
body{font-family:'Oswald',sans-serif;font-weight:300;color:var(--white);background:var(--ink);position:relative}
.band{position:absolute;left:0;width:998px}
.wrap{position:absolute;left:158px;width:684px;top:0;height:100%}
ul{list-style:none}

/* header */
.header{top:0;height:82px;background:var(--sky)}
.brand{position:absolute;left:0;top:22px;display:flex;align-items:center;gap:8px}
.brand-mark{width:30px;height:30px;border-radius:50%;background:var(--white)}
.brand-name{font-size:30px;font-weight:400;line-height:1;color:var(--white)}
.brand-tag{position:absolute;left:38px;top:34px;font-size:11px;font-family:Arial,sans-serif;white-space:nowrap}
.contact-top{position:absolute;right:0;top:32px;text-align:right}
.phone{font-size:12px;font-weight:400}
.cta{display:inline-block;margin-top:4px;background:var(--coral);font-size:11px;padding:4px 6px}

/* nav */
.nav{top:82px;height:34px;background:var(--navy)}
.menu{position:absolute;left:0;top:0;height:34px;display:flex;align-items:center;font-size:11px;font-weight:400}
.menu li{padding:0 13px;border-left:1px solid var(--white);line-height:10px}
.menu li:last-child{border-right:1px solid var(--white)}
.menu li:first-child{padding-left:15px}
.menu .active{color:var(--coral)}
.search{position:absolute;right:0;top:10px;display:flex}
.search-field{width:98px;height:15px;background:var(--white);color:#999;font-size:7px;font-family:Arial,sans-serif;font-style:italic;padding:3px 5px}
.search-btn{width:20px;height:15px;background:var(--coral);display:flex;align-items:center;justify-content:center}

/* hero */
.hero{top:116px;height:216px;background:var(--sky)}
.video{position:absolute;left:0;top:36px;width:213px;height:145px;background:linear-gradient(135deg,#9aa7b3,#d8dee4 50%,#5a6470);border:1px solid var(--white)}
.play{position:absolute;left:79px;top:54px}
.perks{position:absolute;left:224px;top:36px;font-size:10.5px;line-height:18.5px}
.enroll{position:absolute;left:475px;top:6px;width:209px;height:204px;background:var(--navy);padding:8px 12px}
.enroll h2{text-align:center;font-size:15px;font-weight:400;margin-bottom:8px}
.field{height:21px;background:var(--white);color:#666;font-size:9px;padding:4px 5px;margin-bottom:6px;position:relative}
.field .arrow{position:absolute;right:0;top:0;width:18px;height:21px;background:var(--coral)}
.field .arrow:after{content:"";position:absolute;left:5px;top:9px;border:4px solid transparent;border-top-color:var(--white)}
.submit{display:inline-block;background:var(--coral);font-size:10px;font-weight:400;padding:4px 6px}

/* strap */
.strap{top:332px;height:67px;background:var(--ink);text-align:center;font-size:19px;font-weight:400;line-height:67px}

/* main */
.main{top:399px;height:467px;background:var(--mist);color:var(--text)}
.welcome{position:absolute;left:0;top:27px;width:445px}
.section-title{font-size:15px;font-weight:400;margin-bottom:8px}
.welcome p{font-family:Arial,sans-serif;font-size:7.2px;line-height:11px;margin-bottom:8px}
.book{position:absolute;left:475px;top:27px}
.book li{font-size:8.5px;line-height:14.3px;font-weight:400}
.packages-title{position:absolute;left:0;width:684px;top:176px;text-align:center;font-size:23px;font-weight:400}
.card{position:absolute;top:219px;width:209px;height:219px;background:var(--sky);border-radius:4px;padding:6px;color:var(--white)}
.card-head{height:67px;background:var(--navy);display:flex;align-items:center;justify-content:space-between;padding:0 22px}
.card-name{font-size:21px;font-weight:400}
.price{font-size:45px;font-weight:300;line-height:1;position:relative}
.price sup{font-size:15px;position:absolute;left:-10px;top:0}
.card-body{margin-top:5px;height:105px;background:var(--navy);padding:10px 12px;font-size:7.5px;line-height:11px;font-weight:400}
.card-body ul{margin-top:10px}
.card-actions{position:absolute;right:6px;bottom:6px;display:flex;gap:6px;font-size:10px;font-weight:400}
.btn-light{background:var(--white);color:var(--text);padding:4px 6px}
.btn-buy{background:var(--coral);padding:4px 7px}

/* social */
.social{top:866px;height:152px;background:var(--navy)}
.divider{position:absolute;top:14px;width:1px;height:122px;background:#5b92c6}
.net{position:absolute;top:44px;display:flex;gap:12px}
.net-square{width:64px;height:64px;border-radius:6px;background:var(--white);opacity:.9}
.net h3{font-size:14px;font-weight:400;line-height:1.1;margin-top:6px}
.net small{display:block;font-size:7.5px;font-weight:400}
.net-actions{display:flex;gap:12px;margin-top:10px;align-items:center}
.mini{background:#eef2f7;color:#3b5b8c;font-size:7px;padding:2px 4px;border:1px solid #c5cfdc}
.count{background:var(--white);color:#3b5b8c;font-size:8px;padding:4px 8px;font-weight:400;border-radius:2px}
.testimonials{position:absolute;left:475px;top:14px;width:200px}
.testimonials h3{font-size:15px;font-weight:400;margin-left:8px;margin-bottom:6px}
.testimonials p{font-size:7.5px;line-height:14.3px;font-weight:400}
.testimonials a{color:var(--white);font-size:7.5px;font-weight:400}

/* footer */
.footer{top:1018px;height:136px;background:var(--ink)}
.col{position:absolute;top:19px;font-size:8.5px;font-weight:400}
.col h4{font-size:8.5px;font-weight:400;margin-bottom:17px}
.col li{line-height:14.3px}
.contact-list td{padding-right:12px;line-height:14.3px}
.fdiv{position:absolute;top:20px;width:1px;height:96px;background:#4a4445}
.bottom{top:1154px;height:46px;background:var(--ink);border-top:1px solid #3e393a;font-size:6px;font-weight:400}
.legal{position:absolute;left:0;top:12px;line-height:10px}
.links{position:absolute;right:0;top:12px}
</style>
</head>
<body>

<header class="band header">
  <div class="wrap">
    <div class="brand">
      <span class="brand-mark"></span>
      <span class="brand-name">QRAVE</span>
    </div>
    <div class="brand-tag" style="left:80px;top:58px">Online Tuition</div>
    <div class="contact-top">
      <div class="phone">PHONE: 000 000 00000</div>
      <div class="cta">CLICK HERE FOR MORE</div>
    </div>
  </div>
</header>

<nav class="band nav">
  <div class="wrap">
    <ul class="menu">
      <li class="active">HOME</li>
      <li>TUTORIAL PACKAGES</li>
      <li>WEEKLY TIPS AND COMMENTS</li>
      <li>READING</li>
      <li>SPEAKING</li>
      <li>LISTENING</li>
      <li>WRITING</li>
    </ul>
    <div class="search">
      <div class="search-field">Search</div>
      <div class="search-btn">
        <svg width="10" height="10" viewBox="0 0 10 10"><circle cx="4.2" cy="4.2" r="3" fill="none" stroke="#fff" stroke-width="1.3"/><line x1="6.3" y1="6.3" x2="9" y2="9" stroke="#fff" stroke-width="1.3"/></svg>
      </div>
    </div>
  </div>
</nav>

<section class="band hero">
  <div class="wrap">
    <div class="video" role="img" aria-label="Video preview of tutors and students meeting in an office">
      <svg class="play" width="55" height="38" viewBox="0 0 55 38"><rect width="55" height="38" rx="8" fill="#d6453a"/><polygon points="21,10 21,28 36,19" fill="#fff"/></svg>
    </div>
    <ul class="perks">
      <li>• ONLINE TRAINING THROUGH VIDEO CLASSES</li>
      <li>• BULLETPRACTISE EXAMS FOR READING, WRITING &amp; LISTENING</li>
      <li>• BULLETTRAINING FOR ACADEMIC AND GENERAL MODULES</li>
      <li>• BULLETTUTOR ASSISTANCE THROUGH EMAIL &amp; CHAT</li>
      <li>• BULLETYOU CAN TAKE CLASSES ANY WHERE, ANY TIME</li>
      <li>• BULLETALL THESE JUST FOR $99, BUT NOW FROM $25.00</li>
    </ul>
    <form class="enroll">
      <h2>ENROLL NOW</h2>
      <div class="field">Name</div>
      <div class="field">Email</div>
      <div class="field">Telephone</div>
      <div class="field">Address</div>
      <div class="field">Select Clinic<span class="arrow"></span></div>
      <span class="submit">SUBMIT</span>
    </form>
  </div>
</section>

<section class="band strap">PROFESSIONAL HELP FOR PEOPLE TAKING AN QRAVE TEST</section>

<main class="band main">
  <div class="wrap">
    <div class="welcome">
      <h2 class="section-title">WELCOME TO QRAVE ONLINE TUITION</h2>
      <p>Lorem Ipsum is simply dummy text of the printing and typesetting industry. Lorem Ipsum has been the industry's standard dummy text ever since the 1500s, when an unknown printer took a galley of type and scrambled it to make a type specimen book. It has survived not only five centuries, but also the leap into electronic typesetting, remaining essentially unchanged. It was popularised in the 1960s with the release of Tessaprint sheets containing Lorem Ipsum passages, and more recently with desktop publishing software like Pagewright Studio including versions of Lorem Ipsum.</p>
      <p>Lorem Ipsum is simply dummy text of the printing and typesetting industry. Lorem Ipsum has been the industry's standard dummy text ever since the 1500s, when an unknown printer took a galley of type and scrambled it to make a type specimen book.</p>
    </div>
    <div class="book">
      <h2 class="section-title">BOOK COURSE NOW</h2>
      <ul>
        <li>• Online trining through video classes</li>
        <li>• Practise exams for Reading, Writing &amp; Listening</li>
        <li>• Training for Academic and Geaneral Modules</li>
        <li>• Tutor assistance throgh email &amp; chat</li>
        <li>• You can take classes any where, any time</li>
        <li>• All these just for $99, But now from $25.00</li>
      </ul>
    </div>

    <h2 class="packages-title">TUTORIAL PACKAGES</h2>

    <article class="card" style="left:0">
      <div class="card-head"><span class="card-name">GOLD</span><span class="price"><sup>$</sup>49</span></div>
      <div class="card-body">Last minute QRAVE preparation.<br>Ideal for thosewho need to get familiar with test format and strategies.
        <ul><li>• LOREM IPSUM</li><li>• LOREM IPSUM</li><li>• LOREM IPSUM</li><li>• LOREM IPSUM</li></ul></div>
      <div class="card-actions"><span class="btn-light">READ MORE</span><span class="btn-buy">BUY</span></div>
    </article>
    <article class="card" style="left:237px">
      <div class="card-head"><span class="card-name">DIAMOND</span><span class="price"><sup>$</sup>99</span></div>
      <div class="card-body">Last minute QRAVE preparation.<br>Ideal for thosewho need to get familiar with test format and strategies.
        <ul><li>• LOREM IPSUM</li><li>• LOREM IPSUM</li><li>• LOREM IPSUM</li><li>• LOREM IPSUM</li></ul></div>
      <div class="card-actions"><span class="btn-light">READ MORE</span><span class="btn-buy">BUY</span></div>
    </article>
    <article class="card" style="left:475px">
      <div class="card-head"><span class="card-name">SILVER</span><span class="price"><sup>$</sup>299</span></div>
      <div class="card-body">Last minute QRAVE preparation.<br>Ideal for thosewho need to get familiar with test format and strategies.
        <ul><li>• LOREM IPSUM</li><li>• LOREM IPSUM</li><li>• LOREM IPSUM</li><li>• LOREM IPSUM</li></ul></div>
      <div class="card-actions"><span class="btn-light">READ MORE</span><span class="btn-buy">BUY</span></div>
    </article>
  </div>
</main>

<section class="band social">
  <div class="wrap">
    <div class="net" style="left:0">
      <span class="net-square"></span>
      <div>
        <h3>WE'RE ON GATHERLY</h3>
        <small>LIKE US TO SEE OUR DAILY UPDATES!</small>
        <div class="net-actions"><span class="mini">Like</span><span class="count">20</span></div>
      </div>
    </div>
    <span class="divider" style="left:218px"></span>
    <div class="net" style="left:237px">
      <span class="net-square"></span>
      <div>
        <h3>WE'RE ON CHIRRUP</h3>
        <small>LIKE US TO SEE OUR DAILY UPDATES!</small>
        <div class="net-actions"><span class="mini">Share</span><span class="count">241</span></div>
      </div>
    </div>
    <span class="divider" style="left:455px"></span>
    <div class="testimonials">
      <h3>TESTIMONIALS</h3>
      <p>Lorem Ipsum is simply dummy text of the printing and typesetting industry. Lorem Ipsum has been the industry's standard dummy text ever since the 1500s, when an unknown printer took a galley of type and scrambled it to make a type specimen book.</p>
      <a href="#">READ MORE</a>
    </div>
  </div>
</section>

<footer class="band footer">
  <div class="wrap">
    <div class="col" style="left:0">
      <h4>QRAVE ONLINE TUITION DOWNLOADS</h4>
      <ul><li>• Droidell</li><li>• Slatepad</li><li>• Penguix</li><li>• Orchard OS</li><li>• Panefold</li></ul>
    </div>
    <span class="fdiv" style="left:218px"></span>
    <div class="col" style="left:236px">
      <h4>CONTACT</h4>
      <table class="contact-list">
        <tr><td>Apply</td><td>: Contact me</td></tr>
        <tr><td>Email</td><td>: qrave@mailnest.example</td></tr>
        <tr><td>Mobile</td><td>: +000 000 00000</td></tr>
        <tr><td>Talvo</td><td>: qrave</td></tr>
      </table>
    </div>
    <span class="fdiv" style="left:455px"></span>
    <div class="col" style="left:475px">
      <h4>EXTRAS</h4>
      <ul><li>Downloads</li><li>Placement test</li><li>Screenshots</li><li>Topics</li><li>Videos</li></ul>
    </div>
  </div>
</footer>

<div class="band bottom">
  <div class="wrap">
    <div class="legal">Page last updated: 1/12/2014<br>2005-2014 QRAVE Online Tuition.</div>
    <div class="links">Home | Tutorial Packages | Weekly Tips and Comments | Reading | Speaking | Listening | Writing</div>
  </div>
</div>

</body>
</html>
```